E-Commerce Website Update for Bamboo Poles Company

Existing website at:

http://www.reedcraftstudio.example/
http://www.reedcraftstudio.example/pages/product-and-price-list

Two pages to design: home page and "price list" page.

Info for home page as follows:

HOME PAGE:

Header:
Company Name: reedcraft studio
Telephone: 1 888 412 5093

Across the top:
Home | Price List | Blog | FAQ | About | Contact

Down the side:
About Bamboo
Wedding Arbors
Bamboo For Flutes
Black Bamboo
Spotted Bamboo
Bamboo Carpentry
Photo Gallery
All Products & Prices
Blog
FAQ
About
Contact

Should have shopping cart and search buttons on top.
Please see ai file, attached for logo (leaf) and font
In addition the homepage should have one or two sections for promotions

Chosen design will be asked to help deign a PRODUCT AND PRICE LIST page similar to the one we have now, but with "LEARN MORE" and "ORDER NOW" buttons for each item.
Updates

Reason: Thanks  for all the designs so far; giving an extra week for extra consideration.

Target Market(s)

Consumers, wedding planners.

Industry/Entity Type

Shopping

Requirements
Must have
• Clean, easy to read design.
Should not have
• No flash animation.

```html
<!DOCTYPE html>
<html lang="en">
<head>
<meta charset="utf-8">
<title>reedcraft studio — Home</title>
<link rel="stylesheet" href="https://fonts.googleapis.com/css2?family=Arimo:wght@400;700&family=Libre+Baskerville&display=swap">
<style>
  :root {
    --grass-dark: #2f6a1f;
    --grass-mid: #4f8a34;
    --grass-light: #7fae5c;
    --band-green: #137a2e;
    --band-dark: #0f6526;
    --side-green: #3a6b52;
    --cart-green: #3d6b55;
    --nav-active: #b994a7;
    --ink: #111111;
    --white: #ffffff;
    --rule: #c9c9c9;
    --btn-top: #9fb3a9;
    --btn-bottom: #5b7d6b;
    --learn-top: #4f7c63;
    --learn-bottom: #2f5a43;
  }
  * { box-sizing: border-box; margin: 0; padding: 0; }
  html, body { width: 1135px; height: 1200px; overflow: hidden; background: var(--white); }
  body { font-family: "Arimo", Arial, sans-serif; color: var(--ink); }
  .page { position: relative; width: 1135px; height: 1200px; overflow: hidden; }

  .backdrop {
    position: absolute; left: 0; top: 0; width: 1135px; height: 660px;
    background:
      linear-gradient(to bottom, rgba(255,255,255,0) 0%, rgba(255,255,255,0) 78%, rgba(255,255,255,1) 100%),
      linear-gradient(135deg, var(--grass-mid) 0%, var(--grass-light) 30%, var(--grass-dark) 60%, var(--grass-mid) 100%);
  }

  .brand { position: absolute; left: 37px; top: 6px; font-weight: 700; line-height: 1; }
  .brand-main { display: block; font-size: 45px; color: var(--ink); letter-spacing: -0.5px; }
  .brand-sub { display: block; font-size: 27px; color: var(--white); margin-top: 6px; }

  .search { position: absolute; left: 922px; top: 14px; width: 154px; height: 25px; display: flex; }
  .search-field { flex: 1; background: var(--white); border: 1px solid #6b8f5c; }
  .search-btn { width: 24px; height: 25px; background: #eef3f6; border: 1px solid #6b8f5c; display: flex; align-items: center; justify-content: center; }

  .cart { position: absolute; left: 892px; top: 45px; width: 224px; height: 46px; background: var(--cart-green); color: var(--white); display: flex; align-items: center; padding-left: 14px; gap: 8px; }
  .cart-title { font-size: 19px; line-height: 1; }
  .cart-count { font-size: 11px; font-weight: 700; margin-top: 2px; }

  .topnav { position: absolute; left: 23px; top: 92px; width: 1092px; height: 50px; background: var(--white); display: flex; align-items: center; }
  .topnav a { color: var(--ink); text-decoration: none; font-size: 20px; padding: 0 11px; height: 46px; line-height: 46px; }
  .topnav a.is-active { background: var(--nav-active); color: var(--white); margin-left: 11px; }
  .callus { margin-left: auto; display: flex; align-items: center; gap: 10px; padding-right: 15px; font-size: 20px; }

  .hero { position: absolute; left: 23px; top: 148px; width: 1092px; height: 476px;
    background: linear-gradient(90deg, #b5a86b 0%, #d9d3b0 18%, #a79a5c 35%, #e4e2d6 52%, #b8ab6e 70%, #dedcd0 85%, #a39655 100%); }
  .welcome { position: absolute; left: 207px; top: 378px; width: 608px; height: 226px; background: rgba(255,255,255,0.82); border-radius: 4px; padding: 10px 17px; }
  .welcome h1 { font-weight: 400; font-size: 25px; margin-bottom: 8px; }
  .welcome p { font-size: 14.4px; line-height: 24px; }
  .btn-learn { position: absolute; right: 9px; bottom: 7px; width: 116px; height: 34px; border-radius: 4px; background: linear-gradient(var(--learn-top), var(--learn-bottom)); color: var(--ink); font-size: 15px; display: flex; align-items: center; justify-content: center; }

  .catbar { position: absolute; left: 22px; top: 625px; width: 1093px; height: 53px; background: var(--band-green); border-radius: 12px 12px 0 0; }
  .catbar span { position: absolute; top: 7px; height: 39px; background: var(--band-dark); color: var(--white); border-radius: 3px; display: flex; align-items: center; justify-content: center; font-size: 18px; }
  .catbar .nav-label { font-size: 26px; }

  .sidenav { position: absolute; left: 22px; top: 678px; width: 250px; height: 457px; background: var(--side-green); padding: 28px 0 0 32px; }
  .sidenav a { display: block; width: 183px; color: var(--white); text-decoration: none; font-family: "Libre Baskerville", Georgia, serif; font-size: 17px; line-height: 33px; border-bottom: 1px dotted #b9cfc3; margin-bottom: 2px; }
  .sidenav a:last-child { border-bottom: none; }

  .products { position: absolute; left: 272px; top: 678px; width: 843px; height: 466px; display: grid; grid-template-columns: repeat(4, 1fr); grid-template-rows: 198px 268px; }
  .product { position: relative; border-right: 1px solid var(--rule); border-bottom: 1px solid var(--rule); }
  .product:nth-child(4n) { border-right: 1px solid var(--rule); }
  .product-photo { position: absolute; left: 50%; transform: translateX(-50%); top: 7px; }
  .row-2 .product-photo { top: 10px; }
  .tone-natural { background: linear-gradient(90deg, #c7bd7e, #9c9252, #d6cf9a, #a59a5b); }
  .tone-black { background: linear-gradient(90deg, #f4f4f4, #2b2622 20%, #f4f4f4 35%, #3a332d 50%, #f4f4f4 65%, #2b2622 80%, #f4f4f4); }
  .tone-spotted { background: linear-gradient(90deg, #5b4a36, #8b7656 30%, #fff 45%, #fff 52%, #6a5840 60%, #8e7a58); }
  .tone-arbor { background: linear-gradient(#f2f0ea, #e3dfd2); border: 1px solid #d2cbb4; }
  .product-info { position: absolute; left: 12px; font-size: 11px; font-weight: 700; line-height: 15px; }
  .row-1 .product-info { top: 110px; }
  .row-2 .product-info { top: 167px; }
  .product-actions { position: absolute; left: 10px; right: 14px; display: flex; justify-content: space-between; }
  .row-1 .product-actions { top: 162px; }
  .row-2 .product-actions { top: 218px; }
  .btn-small { width: 81px; height: 31px; border-radius: 4px; background: linear-gradient(var(--btn-top) 0%, #7f9a8b 50%, var(--btn-bottom) 100%); font-size: 11.5px; font-weight: 700; display: flex; align-items: center; justify-content: center; }

  .footer { position: absolute; left: 0; top: 1144px; width: 1135px; height: 56px; background: var(--band-green); color: var(--white); font-size: 11.5px; padding: 11px 0 0 56px; line-height: 24px; }
</style>
</head>
<body>
<div class="page">
  <div class="backdrop" role="img" aria-label="Green grass texture background"></div>

  <div class="brand"><span class="brand-main">reedcraft</span><span class="brand-sub">studio</span></div>

  <div class="search">
    <div class="search-field"></div>
    <div class="search-btn">
      <svg width="16" height="16" viewBox="0 0 16 16"><circle cx="6.5" cy="6.5" r="4.5" fill="#cde6f5" stroke="#2f6da3" stroke-width="1.6"/><line x1="10" y1="10" x2="14.5" y2="14.5" stroke="#2f6da3" stroke-width="2.2" stroke-linecap="round"/></svg>
    </div>
  </div>

  <div class="cart">
    <svg width="36" height="30" viewBox="0 0 36 30"><path d="M2 4h6l4 16h17l4-12H10" fill="none" stroke="#d8e8dc" stroke-width="2.4" stroke-linejoin="round"/><circle cx="14" cy="25" r="2.6" fill="#d8e8dc"/><circle cx="27" cy="25" r="2.6" fill="#d8e8dc"/></svg>
    <div><div class="cart-title">Cart</div><div class="cart-count">Now 0 Items in your Cart</div></div>
  </div>

  <nav class="topnav">
    <a class="is-active" href="#">Home</a>
    <a href="#">Price List</a>
    <a href="#">Blog</a>
    <a href="#">FAQ</a>
    <a href="#">About</a>
    <a href="#">Contact</a>
    <div class="callus">
      <svg width="40" height="40" viewBox="0 0 40 40"><rect x="1" y="1" width="38" height="38" rx="6" fill="#1f8a2f"/><rect x="13" y="6" width="14" height="28" rx="3" fill="#222"/><rect x="15" y="9" width="10" height="9" fill="#9fd3a8"/><g fill="#ddd"><rect x="15" y="21" width="3" height="2"/><rect x="19" y="21" width="3" height="2"/><rect x="23" y="21" width="2" height="2"/><rect x="15" y="25" width="3" height="2"/><rect x="19" y="25" width="3" height="2"/><rect x="23" y="25" width="2" height="2"/></g></svg>
      <span>Call Us: 1 888 412 5093</span>
    </div>
  </nav>

  <div class="hero" role="img" aria-label="Photo of a family peeking out from between tall natural bamboo poles"></div>

  <section class="welcome">
    <h1>Welcome to your Pole Provider</h1>
    <p>Bamboo poles at wholesale prices direct from Reedcraft Studio.<br>
    Need bamboo poles at a competitive price? Welcome to your one-stop pole shop.
    We warehouse a variety of types poles in a variety of diameters, from 5/8" to 5 1/2",
    in lengths up to 8'. We have natural poles, moso (mao) timber poles, black poles
    spotted poles… and regular bamboo poles. Whatever your project may be, from
    flutes to weddings to roasting a pig, we have the perfect pole for you.</p>
    <span class="btn-learn">LEARN MORE</span>
  </section>

  <div class="catbar">
    <span class="nav-label" style="left:18px;width:218px;">Navigation</span>
    <span style="left:289px;width:128px;">Bamboo Poles</span>
    <span style="left:493px;width:122px;">Black Poles</span>
    <span style="left:694px;width:134px;">Spotted Poles</span>
    <span style="left:872px;width:213px;">Bamboo Wedding Arbors</span>
  </div>

  <nav class="sidenav">
    <a href="#">About Bamboo</a>
    <a href="#">Wedding Arbors</a>
    <a href="#">Bamboo For Flutes</a>
    <a href="#">Black Bamboo</a>
    <a href="#">Spotted Bamboo</a>
    <a href="#">Bamboo Carpentry</a>
    <a href="#">Photo Gallery</a>
    <a href="#">All Products &amp; Prices</a>
    <a href="#">Blog</a>
    <a href="#">FAQ</a>
    <a href="#">About</a>
    <a href="#">Contact</a>
  </nav>

  <section class="products">
    <div class="product row-1"><div class="product-photo tone-natural" role="img" aria-label="Natural bamboo poles" style="width:56px;height:86px;"></div><div class="product-info">Item number:A1<br>Lorem icing elit<br>$ 15.98</div><div class="product-actions"><span class="btn-small">DETAILS</span><span class="btn-small">ORDER NOW</span></div></div>
    <div class="product row-1"><div class="product-photo tone-black" role="img" aria-label="Black bamboo poles" style="width:50px;height:78px;"></div><div class="product-info">Item number:A1<br>Lorem icing elit<br>$ 15.98</div><div class="product-actions"><span class="btn-small">DETAILS</span><span class="btn-small">ORDER NOW</span></div></div>
    <div class="product row-1"><div class="product-photo tone-spotted" role="img" aria-label="Spotted bamboo poles" style="width:68px;height:78px;"></div><div class="product-info">Item number:A1<br>Lorem icing elit<br>$ 15.98</div><div class="product-actions"><span class="btn-small">DETAILS</span><span class="btn-small">ORDER NOW</span></div></div>
    <div class="product row-1"><div class="product-photo tone-arbor" role="img" aria-label="Bamboo wedding arbor" style="width:90px;height:44px;"></div><div class="product-info">Item number:A1<br>Lorem icing elit<br>$ 15.98</div><div class="product-actions"><span class="btn-small">DETAILS</span><span class="btn-small">ORDER NOW</span></div></div>
    <div class="product row-2"><div class="product-photo tone-natural" role="img" aria-label="Close-up of natural bamboo poles" style="width:72px;height:76px;"></div><div class="product-info">Item number:A1<br>Lorem icing elit<br>$ 15.98</div><div class="product-actions"><span class="btn-small">DETAILS</span><span class="btn-small">ORDER NOW</span></div></div>
    <div class="product row-2"><div class="product-photo tone-black" role="img" aria-label="Close-up of black bamboo poles" style="width:52px;height:98px;"></div><div class="product-info">Item number:A1<br>Lorem icing elit<br>$ 15.98</div><div class="product-actions"><span class="btn-small">DETAILS</span><span class="btn-small">ORDER NOW</span></div></div>
    <div class="product row-2"><div class="product-photo tone-spotted" role="img" aria-label="Close-up of spotted bamboo poles" style="width:68px;height:96px;"></div><div class="product-info">Item number:A1<br>Lorem icing elit<br>$ 15.98</div><div class="product-actions"><span class="btn-small">DETAILS</span><span class="btn-small">ORDER NOW</span></div></div>
    <div class="product row-2"><div class="product-photo tone-arbor" role="img" aria-label="Bamboo wedding arbor frame" style="width:100px;height:80px;"></div><div class="product-info">Item number:A1<br>Lorem icing elit<br>$ 15.98</div><div class="product-actions"><span class="btn-small">DETAILS</span><span class="btn-small">ORDER NOW</span></div></div>
  </section>

  <footer class="footer">
    <div>Copyright © 2011 Reedcraft Studio. All Rights Reserved. All prices USD.</div>
    <div>Designed by northpine webworks and powered by Cartwell.</div>
  </footer>
</div>
</body>
</html>
```